Silver Fern Tagline: Beauty & Balance

I’m looking to create a professional website for my body sculpting, facial, waxing, and wellness spa. I’d like clarity on all required components and integrations needed for a fully functional, client‑friendly platform.**

The website should include:

- **Home Page**
- **About Page**
- **Contact Page**
- **Services Page** (with detailed service descriptions)
- **Meet the Team Page**
- **Product Page** (with e‑commerce capabilities)
- **Blog Section** (multiple posts/pages)
**** Education-
- **Refund & Cancellation Policies Page, Legal Polices ( to discuss potient risk when using products and equipment for services rendered *

**Functionality Requirements: **

- Seamless **integration with external platforms** used for scheduling, client management, or marketing.
- Full **e‑commerce capability**, including:
- “Buy Now” Pay Later” solutions like Paylater-X, Vorlo, Tessel and Integration with **Maple Payments** and similar financing providers
- Ability to manage and sell both **services and retail products**.
- A user‑friendly backend for updating content, products, and blog posts.

Technical Requirements
• HIPAA Compliance: Use platforms like Korvia or GlowDeskPro to ensure client health data and photos are stored securely. HIPAA Notice: Since you offer post-op services, include a small disclaimer below your contact form: "Please do not share sensitive medical information through this form. Private health details will be collected during your secure, HIPAA-compliant intake process".

• Mobile Optimization: Ensure the site is "responsive" so it looks perfect on smartphones where most clients will book.
• SEO: Include local keywords like "Sacramento Body Contouring" and "Best Waxing in 95734" to help people find you.

I’m seeking guidance on what is required to build this site effectively, including platform recommendations, integrations, and any technical considerations.

Silver Fern
Tagline : Beauty and Balance

Logo- I created this logo attached. I want this concept but want it revised properly and I am willing to pay for a revised logo which will not be too far off from what you currently see.

Industry/Entity Type

Beauty, Cosmetic, Spa, Wellness, Holistic

Coding

Coded - Design and coding required

Number of Pages Required

5+ page

```html
<!DOCTYPE html>
<html lang="en">
<head>
<meta charset="utf-8">
<title>Silver Fern</title>
<link rel="stylesheet" href="https://fonts.googleapis.com/css2?family=Cinzel:wght@400;500;600&family=Montserrat:wght@400;500;600;700&family=Libre+Baskerville&display=swap">
<style>
:root{
  --board:#808080;
  --white:#ffffff;
  --pink:#c8288a;
  --pink-hot:#e0469f;
  --tan:#d3a86c;
  --gold:#d7a21b;
  --gold-dark:#a8740c;
  --cream:#fdf9ea;
  --blush:#f4d3dc;
  --green:#3bbf8a;
  --ink:#1d1d1d;
  --black:#000000;
  --serif:"Cinzel", serif;
  --sans:"Montserrat", sans-serif;
  --book:"Libre Baskerville", serif;
}
*{box-sizing:border-box;margin:0;padding:0}
html,body{width:1200px;height:2192px;overflow:hidden;background:var(--board)}
.board{position:absolute;left:0;top:0;width:1410px;height:2576px;transform:scale(0.851064);transform-origin:0 0;background:var(--board)}
.page{position:absolute;top:45px;width:628px;background:var(--white);overflow:hidden;font-family:var(--sans);color:var(--ink)}
.page--a{left:42px;height:2407px}
.page--b{left:727px;height:2475px}
.abs{position:absolute}

.site-header{position:absolute;left:0;top:0;width:628px;height:53px;background:var(--white);border-top:3px solid;border-image:linear-gradient(90deg,#fff 0 45%,var(--pink-hot) 60%,#e77fc0 100%) 1;z-index:5}
.brand{position:absolute;left:38px;top:0;width:125px;height:100px;background:var(--white);border-radius:0 0 62px 62px;z-index:6;display:flex;align-items:center;justify-content:center;padding-top:6px}
.brand__name{font-family:var(--serif);font-size:12px;font-weight:500;color:var(--pink);letter-spacing:.5px}
.nav a{position:absolute;top:24px;font-family:var(--serif);font-size:7px;color:#333;text-decoration:none;letter-spacing:.3px}
.nav a.is-active{color:var(--pink-hot)}
.btn{position:absolute;display:flex;align-items:center;justify-content:center;border-radius:16px;font-family:var(--serif);font-size:7.5px;font-weight:600;letter-spacing:.4px;text-decoration:none;white-space:nowrap}
.btn--grad{background:linear-gradient(90deg,var(--tan),var(--pink-hot));color:#fff}
.btn--white{background:#fff;color:var(--pink)}

.hero{position:absolute;left:0;top:0;width:628px;height:430px}
.hero__title{position:absolute;left:58px;top:148px;font-family:var(--serif);font-size:25px;line-height:33px;color:#fff;letter-spacing:.5px;font-weight:400}
.hero__sub{position:absolute;left:58px;top:218px;font-size:7.6px;font-weight:700;line-height:15px;color:#fff}
.emblem{position:absolute;width:38px;height:38px;border-radius:50%;background:#fff;box-shadow:0 0 0 3px rgba(255,255,255,.5),0 2px 6px rgba(0,0,0,.15);display:flex;align-items:center;justify-content:center}
.emblem::after{content:"";width:16px;height:16px;border-radius:50%;background:linear-gradient(135deg,var(--pink-hot),var(--green))}

.h-section{position:absolute;left:0;width:628px;text-align:center;font-family:var(--serif);font-size:20px;font-weight:500;color:var(--pink);letter-spacing:.8px;line-height:28px}
.copy{font-size:6.7px;line-height:13.4px;color:#444}

.about-mark{position:absolute;left:28px;top:430px;width:260px;height:245px;display:flex;align-items:center;justify-content:center;background:#fffdf8}
.about-mark__name{font-family:var(--serif);font-size:24px;font-weight:500;color:var(--pink)}

.card{position:absolute;width:164px;height:170px}
.card__img{position:absolute;left:0;top:0;width:164px;height:134px}
.card__body{position:absolute;left:10px;top:96px;width:143px;height:73px;background:#fff;padding:10px 10px 0;box-shadow:0 2px 6px rgba(0,0,0,.08)}
.card__title{font-size:8.3px;font-weight:500;letter-spacing:.2px}
.card__text{font-size:5.8px;line-height:11px;color:#777;margin-top:4px}
.card__link{font-size:6.2px;color:var(--pink);margin-top:4px}
.arrow{position:absolute;width:15px;height:15px}

.post-lg{position:absolute;left:58px;width:249px;height:255px}
.post-lg__box{position:absolute;left:13px;top:172px;width:220px;height:70px;background:#fff;padding:9px 10px}
.post-sm{position:absolute;left:318px;width:252px;height:122px;border:1px solid #ddd;background:#fff}
.post-sm__img{position:absolute;left:0;top:0;width:104px;height:120px}
.post-sm__body{position:absolute;left:124px;top:16px;width:118px}
.post-date{font-size:6px;color:var(--pink);font-weight:500;display:flex;align-items:center;gap:3px}
.post-title{font-family:var(--book);font-size:8.4px;line-height:12.5px;color:#222;margin-top:5px}
.post-text{font-size:6.2px;line-height:11.5px;color:#777;margin-top:5px}

.promo{position:absolute;left:58px;width:512px;height:198px;background:var(--blush)}
.promo__img{position:absolute;left:0;top:0;width:250px;height:198px}
.promo__title{position:absolute;left:272px;top:40px;font-family:var(--serif);font-size:18px;line-height:25px;color:var(--pink);letter-spacing:.4px;font-weight:400}
.promo__note{position:absolute;left:272px;top:102px;font-size:11px;color:#333}
.promo__phone{position:absolute;left:272px;top:125px;font-size:25px;font-weight:600;color:var(--green);letter-spacing:.3px}

.edu-copy{position:absolute;left:100px;width:428px;text-align:center;font-size:6.8px;line-height:15.6px;color:#444}

.footer{position:absolute;left:0;width:628px}
.footer__brand{position:absolute;left:70px;width:120px;text-align:center}
.footer__name{font-family:var(--serif);font-size:13px;font-weight:500;color:var(--pink-hot)}
.footer__col{position:absolute}
.footer__head{font-family:var(--serif);font-size:8.5px;color:#fff;letter-spacing:.3px}
.footer__list{list-style:none;margin-top:10px}
.footer__list li{font-size:6.6px;color:#fff;height:18px;display:flex;align-items:center;gap:5px}
.footer__list li::before{content:"➔";font-size:6.5px}
.contact-row{display:flex;align-items:flex-start;gap:7px;font-size:6.5px;color:#fff;line-height:12px;margin-top:8px}
.contact-row svg{flex:none}
.footer__rule{position:absolute;left:58px;width:512px;height:1px;background:#333}
.footer__copy{position:absolute;left:0;width:628px;text-align:center;font-size:6.6px;font-weight:500;color:#fff}
</style>
</head>
<body>
<svg width="0" height="0" style="position:absolute" aria-hidden="true">
  <defs>
    <linearGradient id="goldGrad" x1="0" y1="0" x2="0" y2="1">
      <stop offset="0" stop-color="#f2c94c"/><stop offset="1" stop-color="#a8740c"/>
    </linearGradient>
    <linearGradient id="heroGrad" x1="0" y1="0" x2="1" y2="1">
      <stop offset="0" stop-color="#a4595c"/><stop offset=".5" stop-color="#c97b7d"/><stop offset="1" stop-color="#d8848f"/>
    </linearGradient>
    <linearGradient id="bandGrad" x1="0" y1="0" x2="1" y2="1">
      <stop offset="0" stop-color="#d3a86c"/><stop offset=".55" stop-color="#d77ea0"/><stop offset="1" stop-color="#e0469f"/>
    </linearGradient>
  </defs>
</svg>

<div class="board">

<section class="page page--a">
  <header class="site-header">
    <nav class="nav">
      <a class="is-active" style="left:187px">HOME</a><a style="left:236px">ABOUT</a><a style="left:289px">SERVICES</a><a style="left:350px">PRODUCT</a><a style="left:416px">TEAM</a><a style="left:464px">MORE ⌄</a>
    </nav>
    <a class="btn btn--grad" style="left:520px;top:12px;width:75px;height:24px;font-size:6.5px">CONTACT US</a>
  </header>
  <div class="brand"><span class="brand__name">SILVER FERN</span></div>

  <div class="hero">
    <svg class="abs" style="left:0;top:0" width="628" height="430" role="img" aria-label="Portrait of a woman with pink butterflies in her hair">
      <path d="M0,53 H628 V300 C628,370 610,415 575,415 C500,412 420,335 314,335 C208,335 128,412 53,415 C18,415 0,370 0,300 Z" fill="url(#heroGrad)"/>
      <path d="M0,300 C0,370 18,415 53,415 C128,412 208,335 314,335 C420,335 500,412 575,415 C610,415 628,370 628,300" fill="none" stroke="url(#goldGrad)" stroke-width="7"/>
    </svg>
    <h1 class="hero__title">EXPERIENCE<br>BEAUTY &amp; BALANCE</h1>
    <p class="hero__sub">Luxury Facials, Body Sculpting, Waxing &amp; Wellness<br>Treatments in Fairhaven, CA.</p>
    <a class="btn btn--white" style="left:58px;top:258px;width:117px;height:30px">BOOK YOUR SERVICE</a>
    <div class="emblem" style="left:300px;top:311px"></div>
  </div>

  <div class="about-mark"><span class="about-mark__name">SILVER FERN</span></div>
  <h2 class="h-section" style="left:315px;width:300px;text-align:left;top:467px">ABOUT SILVER FERN</h2>
  <div class="abs copy" style="left:314px;top:496px;width:256px;text-align:justify">
    <p>At Silver Fern, we believe beauty is a harmonious blend of inner wellness and outer radiance.Our studio was created to offer a calming escape—where every treatment is customized, every client is cared for, and every visit brings you closer to balance.</p>
    <p style="margin-top:13px">From advanced facials and body sculpting to waxing, post-operative care, and lymphatic drainage, we combine skilled techniques with high-quality products to deliver results you can see and feel. Silver Fern is more than a spa—it's a place where you can relax, rejuvenate, and reconnect with yourself.</p>
  </div>
  <a class="btn btn--grad" style="left:314px;top:640px;width:81px;height:30px">READ MORE</a>

  <svg class="abs" style="left:0;top:700px" width="628" height="520" aria-hidden="true">
    <path d="M0,60 C0,30 30,18 70,18 C150,25 230,75 314,75 C398,75 478,25 558,18 C598,18 628,30 628,60 V450 C628,480 610,500 575,500 C500,495 400,415 314,415 C228,415 128,495 53,500 C18,500 0,480 0,450 Z" fill="url(#bandGrad)"/>
    <path d="M0,60 C0,30 30,18 70,18 C150,25 230,75 314,75 C398,75 478,25 558,18 C598,18 628,30 628,60" fill="none" stroke="url(#goldGrad)" stroke-width="7"/>
    <path d="M0,450 C0,480 18,500 53,500 C128,495 228,415 314,415 C400,415 500,495 575,500 C610,500 628,480 628,450" fill="none" stroke="url(#goldGrad)" stroke-width="7"/>
  </svg>
  <div class="abs" role="img" aria-label="Frangipani flowers" style="left:220px;top:700px;width:188px;height:84px;border-radius:50%;background:radial-gradient(ellipse,#fff4c8 0,#f8cdd8 55%,rgba(248,205,216,0) 72%)"></div>
  <h2 class="h-section" style="top:843px;color:#fff">OUR SERVICES</h2>
  <svg class="arrow" style="left:19px;top:976px" viewBox="0 0 16 16"><circle cx="8" cy="8" r="7" fill="none" stroke="#fff"/><path d="M10,8 H5 M7,5.5 L4.8,8 L7,10.5" stroke="#fff" fill="none"/></svg>
  <svg class="arrow" style="left:594px;top:976px" viewBox="0 0 16 16"><circle cx="8" cy="8" r="7" fill="none" stroke="#fff"/><path d="M6,8 H11 M9,5.5 L11.2,8 L9,10.5" stroke="#fff" fill="none"/></svg>
  <div class="card" style="left:58px;top:899px"><div class="card__img" role="img" aria-label="Facial treatment" style="background:linear-gradient(135deg,#e9d2c8,#c8a59a)"></div><div class="card__body"><p class="card__title">FACIAL TREATMENTS</p><p class="card__text">A fully customized facial designed to restore hydration, improve texture,</p><p class="card__link">Read More</p></div></div>
  <div class="card" style="left:233px;top:899px"><div class="card__img" role="img" aria-label="Body sculpting device session" style="background:linear-gradient(135deg,#e8e2da,#c9b7a5)"></div><div class="card__body"><p class="card__title">BODY SCULPTING</p><p class="card__text">A fully customized facial designed to restore hydration, improve texture,</p><p class="card__link">Read More</p></div></div>
  <div class="card" style="left:407px;top:899px"><div class="card__img" role="img" aria-label="Post-operative care" style="background:linear-gradient(135deg,#e6d6cc,#8fb0d8)"></div><div class="card__body"><p class="card__title">POST-OPERATIVE CARE</p><p class="card__text">A fully customized facial designed to restore hydration, improve texture,</p><p class="card__link">Read More</p></div></div>

  <div class="abs" style="left:0;top:1200px;width:628px;height:900px">
    <h2 class="h-section" style="top:6px">LATEST BLOG</h2>
    <div class="post-lg" style="top:58px"><div class="abs" role="img" aria-label="Body contouring treatment" style="inset:0;background:linear-gradient(160deg,#f3ece6,#e8c9b8)"></div>
      <div class="post-lg__box"><p class="post-date">▦ Jan 20, 2026</p><p class="post-title">Lorem ipsum dolor sit</p><p class="post-text">Lorem ipsum dolor sit amet, consec tet ur adipiscing elit, sed do eiusmod</p></div></div>
    <div class="post-sm" style="top:58px"><div class="post-sm__img" role="img" aria-label="Hand massage" style="background:linear-gradient(135deg,#f2e2d8,#dcb9a4)"></div><div class="post-sm__body"><p class="post-date">▦ Jan 20, 2026</p><p class="post-title">Excepteur sint occaecat cupidatat non</p><p class="post-text">Ut enim ad minim veniam, quis nostrud exercitation ullamco laboris nisi ut aliquip</p></div></div>
    <div class="post-sm" style="top:192px"><div class="post-sm__img" role="img" aria-label="Facial waxing" style="background:linear-gradient(135deg,#eee3dc,#d9b8a6)"></div><div class="post-sm__body"><p class="post-date">▦ Jan 20, 2026</p><p class="post-title">Excepteur sint occaecat cupidatat non</p><p class="post-text">Ut enim ad minim veniam, quis nostrud exercitation ullamco laboris nisi ut aliquip</p></div></div>

    <div class="promo" style="top:370px"><div class="promo__img" role="img" aria-label="Woman with glowing skin" style="background:linear-gradient(90deg,#e3bfae,#f1ccd5)"></div><h3 class="promo__title">AFTER-HOUR<br>SERVICES AVAILABLE</h3><p class="promo__note">By Appointment Only</p><p class="promo__phone">916-555-0142</p></div>

    <h2 class="h-section" style="top:623px">SILVER FERN EDUCATION<br>CENTER</h2>
    <p class="edu-copy" style="top:688px">At Silver Fern, we believe education is just as important as the services we provide. When you understand your body, honor your healing, and learn what's happening beneath the surface, you become empowered to make confident decisions on your journey. This space is designed to help you:Learn how body sculpting actually works, Understand proper aftercare.</p>
    <p class="edu-copy" style="top:767px">Prepare for your appointment, Set healthy, realistic expectations, Protect your health and long-term results, Explore wellness practices you can use at home, Deepen your self-love and healing processThis is your sanctuary for knowledge, growth, and transformation — created to support every step of your journey.</p>
    <a class="btn btn--grad" style="left:221px;top:825px;width:186px;height:30px">EXPLORE THE EDUCATION CENTER</a>
  </div>

  <div class="footer" style="top:2100px;height:307px">
    <svg class="abs" style="left:0;top:0" width="628" height="307" aria-hidden="true">
      <path d="M0,45 C10,85 30,105 60,102 C140,95 220,25 314,25 C408,25 488,95 568,102 C598,105 618,85 628,45 V307 H0 Z" fill="var(--black)"/>
      <path d="M0,45 C10,85 30,105 60,102 C140,95 220,25 314,25 C408,25 488,95 568,102 C598,105 618,85 628,45" fill="none" stroke="url(#goldGrad)" stroke-width="7"/>
    </svg>
    <div class="emblem" style="left:295px;top:4px"></div>
    <div class="footer__brand" style="top:162px"><p class="footer__name">SILVER FERN</p></div>
    <div class="footer__col" style="left:239px;top:128px"><p class="footer__head">QUICK LINKS</p><ul class="footer__list"><li>Home</li><li>About Us</li><li>Services</li><li>Meet The Team</li><li>Contact Us</li></ul></div>
    <div class="footer__col" style="left:346px;top:128px"><p class="footer__head">HELP LINKS</p><ul class="footer__list"><li>FAQ</li><li>Terms of use</li><li>Privacy Policy</li><li>Support Links</li><li>Conditions</li></ul></div>
    <div class="footer__col" style="left:443px;top:128px"><p class="footer__head">CONTACT US</p>
      <div class="contact-row"><svg width="14" height="14" viewBox="0 0 14 14"><circle cx="7" cy="7" r="7" fill="#fff"/><path d="M7,3.5a2.2,2.2 0 0 0-2.2,2.2c0,1.8 2.2,4.3 2.2,4.3s2.2-2.5 2.2-4.3A2.2,2.2 0 0 0 7,3.5z" fill="#000"/></svg><span>Silver Fern<br>United States</span></div>
      <div class="contact-row"><svg width="14" height="14" viewBox="0 0 14 14"><circle cx="7" cy="7" r="7" fill="#fff"/><path d="M4.5,4 l1.3-.3 .8,1.7-.9.7a5,5 0 0 0 2.2,2.2l.7-.9 1.7.8-.3,1.3C7.2,9.6 4.4,6.8 4.5,4z" fill="#000"/></svg><span style="line-height:14px">916-555-0142</span></div>
      <div class="contact-row"><svg width="14" height="14" viewBox="0 0 14 14"><circle cx="7" cy="7" r="7" fill="#fff"/><rect x="3.8" y="4.8" width="6.4" height="4.4" fill="#000"/><path d="M3.8,4.8 L7,7.3 10.2,4.8" stroke="#fff" stroke-width=".6" fill="none"/></svg><span style="line-height:14px">hello@silverfern.com</span></div>
    </div>
    <div class="footer__rule" style="top:255px"></div>
    <p class="footer__copy" style="top:276px">Copyrights@2026.Silver Fern.All Rights Reserved</p>
  </div>
</section>

<section class="page page--b">
  <header class="site-header">
    <nav class="nav">
      <a class="is-active" style="left:187px">HOME</a><a style="left:236px">ABOUT</a><a style="left:289px">SERVICES</a><a style="left:350px">PRODUCT</a><a style="left:416px">TEAM</a><a style="left:464px">MORE ⌄</a>
    </nav>
    <a class="btn btn--grad" style="left:520px;top:12px;width:75px;height:24px;font-size:6.5px">CONTACT US</a>
  </header>
  <div class="brand"><span class="brand__name">SILVER FERN</span></div>

  <div class="hero">
    <svg class="abs" style="left:0;top:0" width="628" height="430" role="img" aria-label="Portrait of a woman with pink butterflies in her hair">
      <path d="M0,53 H628 V300 C628,370 610,415 575,415 C500,412 420,335 314,335 C208,335 128,412 53,415 C18,415 0,370 0,300 Z" fill="url(#heroGrad)"/>
      <path d="M0,300 C0,370 18,415 53,415 C128,412 208,335 314,335 C420,335 500,412 575,415 C610,415 628,370 628,300" fill="none" stroke="url(#goldGrad)" stroke-width="7"/>
    </svg>
    <h1 class="hero__title">EXPERIENCE<br>BEAUTY &amp; BALANCE</h1>
    <p class="hero__sub">Luxury Facials, Body Sculpting, Waxing &amp; Wellness<br>Treatments in Fairhaven, CA.</p>
    <a class="btn btn--white" style="left:58px;top:258px;width:117px;height:30px">BOOK YOUR SERVICE</a>
    <div class="emblem" style="left:300px;top:311px"></div>
  </div>

  <div class="abs" style="left:269px;top:485px;width:322px;height:235px;border-radius:3px;background:linear-gradient(135deg,var(--tan),var(--pink-hot))"></div>
  <div class="abs" role="img" aria-label="Woman relaxing during a facial massage" style="left:59px;top:462px;width:248px;height:238px;border-radius:4px;background:linear-gradient(135deg,#2f3a26,#c9a48e 55%,#e8d2c2)"></div>
  <h2 class="abs" style="left:339px;top:521px;font-family:var(--serif);font-size:20px;font-weight:500;color:#fff;line-height:22px;letter-spacing:.8px">ABOUT SILVER<br>FERN</h2>
  <div class="abs copy" style="left:339px;top:569px;width:232px;color:#fff;font-weight:500;font-size:6.5px">
    <p>At Silver Fern, we believe beauty is a harmonious blend of inner wellness and outer radiance.</p>
    <p style="margin-top:13px">Our studio was created to offer a calming escape—where every treatment is customized, every client is cared for, and every visit brings you closer to balance. Silver Fern is where relaxation meets renewal.</p>
  </div>
  <a class="btn btn--white" style="left:339px;top:670px;width:80px;height:30px">READ MORE</a>

  <svg class="abs" style="left:0;top:757px" width="628" height="525" aria-hidden="true">
    <path d="M0,60 C0,30 30,18 70,18 C150,25 230,75 314,75 C398,75 478,25 558,18 C598,18 628,30 628,60 V450 C628,480 610,503 575,503 C500,498 400,418 314,418 C228,418 128,498 53,503 C18,503 0,480 0,450 Z" fill="var(--cream)"/>
    <path d="M0,60 C0,30 30,18 70,18 C150,25 230,75 314,75 C398,75 478,25 558,18 C598,18 628,30 628,60" fill="none" stroke="url(#goldGrad)" stroke-width="7"/>
    <path d="M0,450 C0,480 18,503 53,503 C128,498 228,418 314,418 C400,418 500,498 575,503 C610,503 628,480 628,450" fill="none" stroke="url(#goldGrad)" stroke-width="7"/>
  </svg>
  <div class="abs" role="img" aria-label="Frangipani flowers" style="left:220px;top:757px;width:188px;height:84px;border-radius:50%;background:radial-gradient(ellipse,#fff4c8 0,#f8cdd8 55%,rgba(248,205,216,0) 72%)"></div>
  <h2 class="h-section" style="top:904px">OUR SERVICES</h2>
  <svg class="arrow" style="left:19px;top:1025px" viewBox="0 0 16 16"><circle cx="8" cy="8" r="7" fill="none" stroke="#222"/><path d="M10,8 H5 M7,5.5 L4.8,8 L7,10.5" stroke="#222" fill="none"/></svg>
  <svg class="arrow" style="left:594px;top:1025px" viewBox="0 0 16 16"><circle cx="8" cy="8" r="7" fill="none" stroke="#222"/><path d="M6,8 H11 M9,5.5 L11.2,8 L9,10.5" stroke="#222" fill="none"/></svg>
  <div class="card" style="left:58px;top:948px"><div class="card__img" role="img" aria-label="Facial treatment" style="background:linear-gradient(135deg,#e9d2c8,#c8a59a)"></div><div class="card__body"><p class="card__title">FACIAL TREATMENTS</p><p class="card__text">A fully customized facial designed to restore hydration, improve texture,</p><p class="card__link">Read More</p></div></div>
  <div class="card" style="left:233px;top:948px"><div class="card__img" role="img" aria-label="Body sculpting device session" style="background:linear-gradient(135deg,#e8e2da,#c9b7a5)"></div><div class="card__body"><p class="card__title">BODY SCULPTING</p><p class="card__text">A fully customized facial designed to restore hydration, improve texture,</p><p class="card__link">Read More</p></div></div>
  <div class="card" style="left:407px;top:948px"><div class="card__img" role="img" aria-label="Post-operative care" style="background:linear-gradient(135deg,#e6d6cc,#8fb0d8)"></div><div class="card__body"><p class="card__title">POST-OPERATIVE CARE</p><p class="card__text">A fully customized facial designed to restore hydration, improve texture,</p><p class="card__link">Read More</p></div></div>

  <div class="abs" style="left:0;top:1250px;width:628px;height:900px">
    <h2 class="h-section" style="top:6px">LATEST BLOG</h2>
    <div class="post-lg" style="top:58px"><div class="abs" role="img" aria-label="Body contouring treatment" style="inset:0;background:linear-gradient(160deg,#f3ece6,#e8c9b8)"></div>
      <div class="post-lg__box"><p class="post-date">▦ Jan 20, 2026</p><p class="post-title">Lorem ipsum dolor sit</p><p class="post-text">Lorem ipsum dolor sit amet, consec tet ur adipiscing elit, sed do eiusmod</p></div></div>
    <div class="post-sm" style="top:58px"><div class="post-sm__img" role="img" aria-label="Hand massage" style="background:linear-gradient(135deg,#f2e2d8,#dcb9a4)"></div><div class="post-sm__body"><p class="post-date">▦ Jan 20, 2026</p><p class="post-title">Excepteur sint occaecat cupidatat non</p><p class="post-text">Ut enim ad minim veniam, quis nostrud exercitation ullamco laboris nisi ut aliquip</p></div></div>
    <div class="post-sm" style="top:192px"><div class="post-sm__img" role="img" aria-label="Facial waxing" style="background:linear-gradient(135deg,#eee3dc,#d9b8a6)"></div><div class="post-sm__body"><p class="post-date">▦ Jan 20, 2026</p><p class="post-title">Excepteur sint occaecat cupidatat non</p><p class="post-text">Ut enim ad minim veniam, quis nostrud exercitation ullamco laboris nisi ut aliquip</p></div></div>

    <div class="promo" style="top:370px"><div class="promo__img" role="img" aria-label="Woman with glowing skin" style="background:linear-gradient(90deg,#e3bfae,#f1ccd5)"></div><h3 class="promo__title">AFTER-HOUR<br>SERVICES AVAILABLE</h3><p class="promo__note">By Appointment Only</p><p class="promo__phone">916-555-0142</p></div>

    <h2 class="h-section" style="top:626px">SILVER FERN EDUCATION<br>CENTER</h2>
    <p class="edu-copy" style="top:691px">At Silver Fern, we believe education is just as important as the services we provide. When you understand your body, honor your healing, and learn what's happening beneath the surface, you become empowered to make confident decisions on your journey. This space is designed to help you:Learn how body sculpting actually works, Understand proper aftercare.</p>
    <p class="edu-copy" style="top:770px">Prepare for your appointment, Set healthy, realistic expectations, Protect your health and long-term results, Explore wellness practices you can use at home, Deepen your self-love and healing processThis is your sanctuary for knowledge, growth, and transformation — created to support every step of your journey.</p>
    <a class="btn btn--grad" style="left:221px;top:832px;width:186px;height:30px">EXPLORE THE EDUCATION CENTER</a>
  </div>

  <div class="footer" style="top:2163px;height:312px">
    <svg class="abs" style="left:0;top:0" width="628" height="312" aria-hidden="true">
      <path d="M0,45 C10,85 30,105 60,102 C140,95 220,25 314,25 C408,25 488,95 568,102 C598,105 618,85 628,45 V312 H0 Z" fill="var(--black)"/>
      <path d="M0,45 C10,85 30,105 60,102 C140,95 220,25 314,25 C408,25 488,95 568,102 C598,105 618,85 628,45" fill="none" stroke="url(#goldGrad)" stroke-width="7"/>
    </svg>
    <div class="emblem" style="left:295px;top:4px"></div>
    <div class="footer__brand" style="top:162px"><p class="footer__name">SILVER FERN</p></div>
    <div class="footer__col" style="left:239px;top:128px"><p class="footer__head">QUICK LINKS</p><ul class="footer__list"><li>Home</li><li>About Us</li><li>Services</li><li>Meet The Team</li><li>Contact Us</li></ul></div>
    <div class="footer__col" style="left:346px;top:128px"><p class="footer__head">HELP LINKS</p><ul class="footer__list"><li>FAQ</li><li>Terms of use</li><li>Privacy Policy</li><li>Support Links</li><li>Conditions</li></ul></div>
    <div class="footer__col" style="left:443px;top:128px"><p class="footer__head">CONTACT US</p>
      <div class="contact-row"><svg width="14" height="14" viewBox="0 0 14 14"><circle cx="7" cy="7" r="7" fill="#fff"/><path d="M7,3.5a2.2,2.2 0 0 0-2.2,2.2c0,1.8 2.2,4.3 2.2,4.3s2.2-2.5 2.2-4.3A2.2,2.2 0 0 0 7,3.5z" fill="#000"/></svg><span>Silver Fern<br>United States</span></div>
      <div class="contact-row"><svg width="14" height="14" viewBox="0 0 14 14"><circle cx="7" cy="7" r="7" fill="#fff"/><path d="M4.5,4 l1.3-.3 .8,1.7-.9.7a5,5 0 0 0 2.2,2.2l.7-.9 1.7.8-.3,1.3C7.2,9.6 4.4,6.8 4.5,4z" fill="#000"/></svg><span style="line-height:14px">916-555-0142</span></div>
      <div class="contact-row"><svg width="14" height="14" viewBox="0 0 14 14"><circle cx="7" cy="7" r="7" fill="#fff"/><rect x="3.8" y="4.8" width="6.4" height="4.4" fill="#000"/><path d="M3.8,4.8 L7,7.3 10.2,4.8" stroke="#fff" stroke-width=".6" fill="none"/></svg><span style="line-height:14px">hello@silverfern.com</span></div>
    </div>
    <div class="footer__rule" style="top:258px"></div>
    <p class="footer__copy" style="top:280px">Copyrights@2026.Silver Fern.All Rights Reserved</p>
  </div>
</section>

</div>
</body>
</html>
```